Flooring Company Wordpress Design Using Elementor

We need a website design using elementor for a flooring company. I have attached a word document with the entire content for the site. I have sample websites www.pellingtonrenovatesutah.com and www.stonepathtilesdenver.com

The site needs to look alot better than the samples. Modern and professional is what we are looking for. 100 times better than the sample websites.

I have images to be used in the site but the file is to large to attached here.

```html
<!DOCTYPE html>
<html lang="en">
<head>
<meta charset="utf-8">
<title>Harborline Floors</title>
<link rel="stylesheet" href="https://fonts.googleapis.com/css2?family=Montserrat:wght@300;400;500;600;700&display=swap">
<style>
:root{
  --orange:#f7941d;
  --ink:#2e2e2e;
  --text:#5c5c5c;
  --muted:#9a9a9a;
  --line:#e6e6e6;
  --footer:#333333;
  --brand:#8a5a2b;
  --white:#ffffff;
}
*{box-sizing:border-box;margin:0;padding:0}
html,body{width:1200px;height:5119px;overflow:hidden}
body{font-family:'Montserrat',sans-serif;color:var(--text);background:var(--white);position:relative}
.abs{position:absolute}
.btn{display:inline-block;background:var(--orange);color:#fff;font-size:14px;font-weight:500;text-transform:uppercase;letter-spacing:.3px;padding:0 18px;height:42px;line-height:42px;border:2px solid #fff;outline:2px solid var(--orange);text-decoration:none;white-space:nowrap}
/* header */
.site-header{left:0;top:0;width:1200px;height:110px;background:#fff}
.brand{left:70px;top:56px;display:flex;align-items:center;gap:10px;white-space:nowrap}
.brand-dot{width:30px;height:30px;border-radius:50%;background:var(--brand)}
.brand-name{font-weight:600;font-size:17px;color:var(--ink)}
.contact{top:10px;display:flex;align-items:center;gap:10px;font-size:13px;color:var(--muted);white-space:nowrap}
.contact .ico{width:42px;height:42px;border:2px solid var(--orange);border-radius:50%;display:flex;align-items:center;justify-content:center}
.nav{top:68px;left:336px;display:flex;gap:42px;font-size:12.5px;text-transform:uppercase;color:#555;white-space:nowrap}
.nav .active{color:var(--orange)}
/* hero */
.hero{left:0;top:110px;width:1200px;height:532px;background:linear-gradient(180deg,#c9c2b6 0%,#9d8670 40%,#6b4a32 100%)}
.hero h1{left:0;top:146px;width:1200px;text-align:center;color:#fff;font-weight:500;font-size:33px;line-height:52px;text-transform:uppercase}
.hero p{left:250px;top:262px;width:700px;text-align:center;color:#fff;font-size:15.5px;line-height:26px;font-weight:400}
.hero .btn{left:488px;top:366px;height:42px;outline:none;border:none;font-size:14px}
/* feature tiles */
.tile{top:642px;width:400px;height:346px;color:#fff;text-align:center}
.tile h3{font-weight:400;font-size:33px;line-height:44px}
.tile-1{left:0;background:linear-gradient(160deg,#4a3a30,#6a4c38);border:3px solid var(--orange)}
.tile-1 .inner{padding:30px 26px}
.tile-1 p{font-size:14px;line-height:25.5px;margin-top:18px}
.tile-1 a{display:block;margin-top:26px;color:#fff;font-size:14px;text-decoration:underline}
.tile-2{left:400px;background:linear-gradient(160deg,#5b5049,#8a3f2a)}
.tile-3{left:800px;background:linear-gradient(160deg,#bdbdbb,#e4e2df)}
.tile-2 h3,.tile-3 h3{margin-top:128px}
.warranty{left:430px;top:1013px;height:44px;line-height:44px;font-size:13.5px}
/* about */
.about-text{left:110px;top:1240px;width:480px}
.about-text h2{font-weight:400;font-size:32px;color:var(--ink);margin-bottom:28px}
.about-text p{font-size:15.5px;line-height:27.5px;color:#666}
.about-text .btn{margin-top:26px}
.about-photo{left:618px;top:1174px;width:582px;height:501px;background:linear-gradient(180deg,#eeeae4 0%,#d9d2c8 45%,#2d3d4c 75%,#c8bca9 100%)}
/* services */
.section-title{left:0;width:1200px;text-align:center;font-weight:400;font-size:31px;color:var(--ink)}
.card{width:348px;height:694px;border:1px solid var(--line);box-shadow:0 1px 6px rgba(0,0,0,.08);background:#fff;text-align:center}
.card h3{height:64px;line-height:64px;font-weight:400;font-size:21px;color:var(--ink)}
.card .photo{height:282px}
.card p{font-size:14px;line-height:25.7px;padding:30px 28px 0;height:236px;overflow:hidden;color:#666}
.card .more{display:block;font-size:14px;color:#666;text-decoration:underline;margin-top:-2px}
.card .btn{margin-top:38px;font-size:14px}
/* testimonials */
.quote-card{top:3477px;width:444px;height:342px;border:1px solid var(--line);border-radius:12px;background:#fff;text-align:center;box-shadow:0 1px 6px rgba(0,0,0,.06)}
.quote-card .q{left:36px;top:24px;font-size:120px;line-height:120px;color:#f3eeea;font-family:Georgia,serif}
.avatar{width:74px;height:74px;border-radius:50%;border:3px solid #ddd;background:linear-gradient(180deg,#9aa6b2,#4d5a66);margin:22px auto 14px;position:relative}
.quote-card h4{font-weight:400;font-size:18px;color:var(--ink)}
.quote-card .role{font-style:italic;font-size:13px;color:var(--muted);margin:6px 0 18px}
.quote-card blockquote{font-style:italic;font-size:13px;line-height:22px;color:#777;padding:0 44px}
.dots{left:556px;top:3850px;display:flex;gap:18px}
.dots span{width:12px;height:12px;background:#e2e2e2}
.dots .on{background:var(--orange)}
/* process */
.step{top:4054px;width:260px;text-align:center}
.step svg{display:block;margin:0 auto 24px}
.step h4{font-weight:400;font-size:19px;line-height:25px;color:var(--ink);margin-bottom:16px}
.step p{font-size:13px;line-height:21.5px;color:#777;padding:0 22px}
/* form */
.form-label{width:170px;height:44px;line-height:44px;background:#666;color:#fff;text-align:center;font-size:14px}
.field{width:248px;height:44px;line-height:44px;border:1px solid #ccc;text-align:center;color:#ccc;font-size:14px}
.submit{left:474px;top:4722px;width:172px;height:44px;line-height:44px;padding:0;text-align:center;font-size:15px}
/* footer */
.site-footer{left:0;top:4860px;width:1200px;height:259px;background:var(--footer);color:#fff}
.foot-nav{top:54px;left:0;width:1200px;display:flex;justify-content:center;gap:42px;font-size:12.5px;font-weight:500;text-transform:uppercase}
.social{top:102px;left:496px;display:flex;gap:34px}
.social span{width:44px;height:44px;border:2px solid #fff;display:block}
.legal{top:188px;left:0;width:1200px;text-align:center;font-size:11.5px;font-weight:500;text-transform:uppercase}
.legal i{font-style:normal;margin:0 22px}
.copy{top:232px;left:0;width:1200px;text-align:center;font-size:11.5px}
</style>
</head>
<body>

<header class="site-header abs">
  <div class="brand abs">
    <span class="brand-dot"></span>
    <span class="brand-name">Harborline Floors</span>
  </div>
  <div class="contact abs" style="left:562px">
    <span class="ico"><svg width="18" height="18" viewBox="0 0 24 24" fill="none" stroke="#f7941d" stroke-width="2"><path d="M5 3h4l2 5-3 2a11 11 0 0 0 6 6l2-3 5 2v4a2 2 0 0 1-2 2A17 17 0 0 1 3 5a2 2 0 0 1 2-2z"/></svg></span>555 014 2290
  </div>
  <div class="contact abs" style="left:776px">
    <span class="ico"><svg width="20" height="16" viewBox="0 0 24 18" fill="none" stroke="#f7941d" stroke-width="2"><rect x="1" y="1" width="22" height="16"/><path d="M1 1l11 9 11-9"/></svg></span>hello@harborlinefloors.com
  </div>
  <svg class="abs" style="left:1074px;top:24px" width="16" height="16" viewBox="0 0 24 24" fill="none" stroke="#f7941d" stroke-width="3"><circle cx="10" cy="10" r="7"/><path d="M15 15l7 7"/></svg>
  <nav class="nav abs">
    <span class="active">Home</span><span>Hardwood Installation</span><span>Laminate Installation</span><span>Service Areas</span><span>Request Quote</span>
  </nav>
</header>

<section class="hero abs" role="img" aria-label="Bright living room with freshly installed wide-plank wood flooring">
  <h1 class="abs">Experience premium flooring installation<br>in Central Florida with Harborline Group</h1>
  <p class="abs">Are you tired of having your residential or commercial floors messed up by unprofessional services? Allow Harborline Group to change your floor installation and removal story today with our premium services, creativity, and personalized approach.</p>
  <a class="btn abs">Get your free estimate</a>
</section>

<div class="tile tile-1 abs" role="img" aria-label="Dark interior with wood flooring">
  <div class="inner">
    <h3>Minimal stress on<br>your plate</h3>
    <p>Floor installation or removal can be stressful for both parties. You have to relocate most of your property on the affected area to a new location and adjust your daily operation. The last thing we want to do is add to that.</p>
    <a>Read More</a>
  </div>
</div>
<div class="tile tile-2 abs" role="img" aria-label="Hallway with warm wood floor"><h3>A Floor worthy of<br>your home</h3></div>
<div class="tile tile-3 abs" role="img" aria-label="Empty bright room with light tile floor"><h3>Qualified and<br>certified experts</h3></div>

<a class="btn warranty abs">Backed by 1-year labor warranty</a>

<section class="about-text abs">
  <h2>A Reliable Partner to lean on</h2>
  <p>Harborline Group comes with over 14 years of experience in floor installation. We are specialists when it comes to tile installation, hardwood installation, carpet installation, tile backsplash installation, vinyl installation, laminate floor installation, and floor removal. Over the years, we have come to position ourselves as the professionals hands our customers need for all their installation and removal needs. With us, you can be assured of on-time performance, professional services, and prime craftsmanship.</p>
  <a class="btn">Learn more</a>
</section>
<div class="about-photo abs" role="img" aria-label="Modern kitchen with dark island, pendant lights and wood floor"></div>

<h2 class="section-title abs" style="top:1774px">Make Your Floors Scream Quality and Beauty</h2>

<article class="card abs" style="left:50px;top:1850px">
  <h3>Tile Installation</h3>
  <div class="photo" role="img" aria-label="Installer laying grey tiles on adhesive" style="background:linear-gradient(135deg,#8d8f92,#3f4247)"></div>
  <p>Tile is one durable flooring material that, when placed well, leaves your home or property looking luxurious and inviting. Harborline Group is fitted with expert tile installers who have experience installing anything tile, from tile flooring, bathroom tile, to backsplash tile. Allow us to make</p>
  <a class="more">Learn More</a><a class="btn">Get a free quote</a>
</article>
<article class="card abs" style="left:425px;top:1850px">
  <h3>Hardwood Installation</h3>
  <div class="photo" role="img" aria-label="Hands fitting a hardwood plank" style="background:linear-gradient(135deg,#e6c9a3,#c0844f)"></div>
  <p>Are you looking for the best hardwood installers near you? You are at the right place. Harborline Group is an expert in all kinds of hardwood installation, from solid to engineered hardwood. We will guide you toward choosing the right wood for your home or</p>
  <a class="more">Learn More</a><a class="btn">Get a free quote</a>
</article>
<article class="card abs" style="left:800px;top:1850px">
  <h3>Laminate Installation</h3>
  <div class="photo" role="img" aria-label="Glossy marble-look laminate floor" style="background:linear-gradient(135deg,#9c9c9c,#f1f1f1 50%,#d8d8d8)"></div>
  <p>Adorning your floor with laminate material is often a great option to limit scratches, wear and tear, and improve floor durability. With a lot to consider when it comes to picking the right flooring and having it installed, you need an experienced mind</p>
  <a class="more">Learn More</a><a class="btn">Get a free quote</a>
</article>

<article class="card abs" style="left:50px;top:2610px">
  <h3>Carpet Installation</h3>
  <div class="photo" role="img" aria-label="Installer placing flooring over underlay" style="background:linear-gradient(135deg,#e2e4e6,#6b4a33)"></div>
  <p>Carpet installation is a good way to personalized the theme of your home, improve comfort, warmth, and a luxurious feel. With many carpets to choose from down to the tiring installation process, it can be overwhelming. Our team of professional</p>
  <a class="more">Learn More</a><a class="btn">Get a free quote</a>
</article>
<article class="card abs" style="left:425px;top:2610px">
  <h3>Vinyl Installation</h3>
  <div class="photo" role="img" aria-label="Roll of wood-look vinyl flooring" style="background:linear-gradient(135deg,#f3e6dc,#c06a36)"></div>
  <p>Vinyl flooring is a great option for families and businesses looking for a balance between the deep texture and feel of real wood, tiles, and stones with the durability, resistance, and low maintenance only dreamed of. Harborline Group is here to</p>
  <a class="more">Learn More</a><a class="btn">Get a free quote</a>
</article>
<article class="card abs" style="left:800px;top:2610px">
  <h3>Floor Removal</h3>
  <div class="photo" role="img" aria-label="Worker removing old floor planks" style="background:linear-gradient(135deg,#f4f4f4,#b9a58c)"></div>
  <p>Removing your floor isn't an easy task, whether it is a carpet installation, hardwood, or concrete. It takes a lot of time and is filled with risks. Harborline Group helps you save time and avoid sustaining any injury through the hands of our qualified floor demolition and</p>
  <a class="more">Learn More</a><a class="btn">Get a free quote</a>
</article>

<h2 class="section-title abs" style="top:3402px">Hear Their Stories!</h2>

<div class="quote-card abs" style="left:-106px">
  <div class="avatar" role="img" aria-label="Customer portrait"></div>
  <h4>Marla K Denning</h4><div class="role">Brightmoor, CEO</div>
  <blockquote>"Sed ut perspiciatis unde omnis iste natus error sit voluptatem accusantium doloremque laudantium, totam rem aperiam, eaque ipsa quae ab illo inventore veritatis et quasi architecto beatae vitae dicta sunt explicabo. Nemo enim ipsam voluptatem quia voluptas sit aspernatur aut."</blockquote>
</div>
<div class="quote-card abs" style="left:378px">
  <div class="q abs">&ldquo;</div>
  <div class="avatar" role="img" aria-label="Customer portrait"></div>
  <h4>Celia R Hartwell</h4><div class="role">Brightmoor, CEO</div>
  <blockquote>"Sed ut perspiciatis unde omnis iste natus error sit voluptatem accusantium doloremque laudantium, totam rem aperiam, eaque ipsa quae ab illo inventore veritatis et quasi architecto beatae vitae dicta sunt explicabo. Nemo enim ipsam voluptatem quia voluptas sit aspernatur aut."</blockquote>
</div>
<div class="quote-card abs" style="left:862px">
  <div class="q abs">&ldquo;</div>
  <div class="avatar" role="img" aria-label="Customer portrait"></div>
  <h4>Owen T Barlow</h4><div class="role">Brightmoor, CEO</div>
  <blockquote>"Sed ut perspiciatis unde omnis iste natus error sit voluptatem accusantium doloremque laudantium, totam rem aperiam, eaque ipsa quae ab illo inventore veritatis et quasi architecto beatae vitae dicta sunt explicabo. Nemo enim ipsam voluptatem quia voluptas sit aspernatur aut."</blockquote>
</div>
<div class="dots abs"><span></span><span class="on"></span><span></span><span></span></div>

<h2 class="section-title abs" style="top:3956px">A Simple Repeatable Process</h2>

<div class="step abs" style="left:50px">
  <svg width="64" height="66" viewBox="0 0 64 66" fill="none" stroke="#f7941d" stroke-width="2.5"><rect x="4" y="8" width="56" height="54" rx="3"/><path d="M4 22h56M18 2v12M46 2v12M22 42l8 8 14-16"/></svg>
  <h4>Schedule An<br>Appointment</h4>
  <p>Fill out the form on our site or call us on our hotline to relay your needs and schedule a free site inspection. It is that simple!</p>
</div>
<div class="step abs" style="left:330px">
  <svg width="60" height="60" viewBox="0 0 60 60" fill="none" stroke="#f7941d" stroke-width="2.5"><rect x="4" y="4" width="52" height="52"/><path d="M4 20L20 4M4 36L36 4M4 52L52 4M20 56L56 20M36 56L56 36M20 4l36 36M4 20l36 36M4 4l52 52"/></svg>
  <h4>Your Preferred<br>Floor Material</h4>
  <p>Based on our findings on consultation and our inspection, we will help you figure out the right type of floor for your home or business space.</p>
</div>
<div class="step abs" style="left:610px">
  <svg width="60" height="66" viewBox="0 0 60 66" fill="none" stroke="#f7941d" stroke-width="2.5"><circle cx="30" cy="26" r="22"/><circle cx="30" cy="26" r="14"/><path d="M30 18l3 6 6 1-4 4 1 6-6-3-6 3 1-6-4-4 6-1z M16 44l-8 18 10-4 4 8 6-16 M44 44l8 18-10-4-4 8-6-16"/></svg>
  <h4>Premium<br>Installation</h4>
  <p>After the two stages are done, and you have approved the work date, our professionals for your floor will begin work on your property.</p>
</div>
<div class="step abs" style="left:890px">
  <svg width="62" height="62" viewBox="0 0 62 62" fill="none" stroke="#f7941d" stroke-width="2.5"><circle cx="31" cy="31" r="28"/><circle cx="21" cy="24" r="2" fill="#f7941d"/><circle cx="41" cy="24" r="2" fill="#f7941d"/><path d="M17 36a15 15 0 0 0 28 0"/></svg>
  <h4>A Happy<br>You!</h4>
  <p>With a quality job done, go ahead and enjoy your floors for years to come with minimal maintenance on your side!</p>
</div>

<h2 class="section-title abs" style="top:4420px">Get started now</h2>

<div class="form-label abs" style="left:112px;top:4525px">Appointment</div>
<div class="field abs" style="left:302px;top:4525px">Type of appointment</div>
<div class="field abs" style="left:571px;top:4525px">Closest city</div>
<div class="field abs" style="left:840px;top:4525px">Date</div>
<div class="form-label abs" style="left:112px;top:4620px">Your Info</div>
<div class="field abs" style="left:302px;top:4620px">Name</div>
<div class="field abs" style="left:571px;top:4620px">Contact info</div>
<div class="field abs" style="left:840px;top:4620px">Address</div>
<a class="btn submit abs">Submit</a>

<footer class="site-footer abs">
  <nav class="foot-nav abs"><span>Home</span><span>Hardwood Installation</span><span>Laminate Installation</span><span>Service Areas</span><span>Request Quote</span></nav>
  <div class="social abs"><span></span><span></span><span></span></div>
  <div class="legal abs">Terms &amp; Condition<i>/</i>Privacy Policy<i>/</i>Sitemap</div>
  <div class="copy abs">Copyrights © 2020 All Rights Reserved</div>
</footer>

</body>
</html>
```